Looking for an attention grabbing company marketing brief/portfolio document for potential clients

We are looking for someone to take a number of our existing marketing documents and combine them into a new fresh design that will showcase our experience to our clients. The final design should be less than 5 pages highlighting our company experience and can be used to send to new potential clients.

Target Market(s)

Construction, Project Management, Commercial buildings, Restaurants, Retail

Industry/Entity Type

Consultant

Font styles to use
Sans Serif

Requirements
Must have
• A company overview, benefits, featured projects. Eye catching design that speaks clearly to the experience of our company and why customers should use us. Branding should match our current colour scheme and theme. Our website is cobaltridgebuildworks.com

```html
<!DOCTYPE html>
<html lang="en">
<head>
<meta charset="utf-8">
<title>Cobalt Ridge Buildworks – Company Flyer</title>
<link href="https://fonts.googleapis.com/css2?family=Roboto:wght@400;500;700&display=swap" rel="stylesheet">
<style>
  :root{
    --navy:#2d3a82;
    --orange:#f3a21c;
    --orange-deep:#ee9a12;
    --charcoal:#3b3b3c;
    --paper:#ffffff;
    --header-grey:#d9d9d9;
    --footer-grey:#d6d6d6;
    --ink:#1c1c1c;
    --backdrop:#8a8a8a;
  }
  *{box-sizing:border-box;margin:0;padding:0}
  html,body{width:1200px;height:1200px;overflow:hidden}
  body{background:var(--backdrop);font-family:"Roboto",Arial,sans-serif;position:relative}
  .flyer{position:absolute;left:180px;top:6px;width:840px;height:1188px;background:var(--paper);overflow:hidden}

  .masthead{position:absolute;left:0;top:0;width:840px;height:330px;
    background:linear-gradient(180deg,#e6e6e6,var(--header-grey));
    display:flex;align-items:center;justify-content:center;gap:22px}
  .brand-name{font-weight:700;font-size:60px;color:var(--navy);letter-spacing:-0.5px}
  .brand-dot{width:46px;height:46px;border-radius:50%;background:var(--orange)}

  .about{position:absolute;left:0;top:330px;width:840px;height:240px;background:var(--charcoal);color:#fff}
  .about-stripe-navy{position:absolute;right:48px;top:0;width:56px;height:100%;background:var(--navy)}
  .about-stripe-orange{position:absolute;right:0;top:0;width:48px;height:100%;background:var(--orange-deep)}
  .about-title{position:absolute;left:24px;top:20px;font-size:36px;font-weight:700;letter-spacing:0.5px}
  .about-title .accent{color:var(--orange)}
  .about-rule{position:absolute;left:24px;top:64px;width:440px;height:3px;background:var(--orange)}
  .about-copy{position:absolute;left:20px;top:78px;width:706px;font-size:13.5px;line-height:25px}

  .profile{position:absolute;left:24px;top:590px;width:400px}
  .block{margin-bottom:18px}
  .block h2{font-size:21px;font-weight:500;color:var(--ink);padding-left:12px;border-left:8px solid var(--orange);line-height:26px;margin-bottom:10px}
  .block h2.navy{border-left-color:var(--navy)}
  .block p,.block li{font-size:15px;line-height:20px;color:var(--ink)}
  .block ul{list-style:none}
  .block li::before{content:"• "}

  .offer{position:absolute;left:436px;top:570px;width:400px;height:545px}
  .offer h3{position:absolute;left:10px;top:26px;font-size:20px;font-weight:700;color:var(--navy);line-height:26px}
  .offer-rule{position:absolute;left:10px;top:82px;width:115px;height:2px;background:var(--orange)}
  .offer svg{position:absolute;left:0;top:0}
  .service{position:absolute;font-size:14px;font-weight:700;color:var(--navy);line-height:18px;white-space:nowrap}
  .service.wrap{white-space:normal;font-size:13px;width:250px;line-height:17px}

  .footer{position:absolute;left:0;top:1115px;width:840px;height:73px;background:var(--footer-grey)}
  .footer-brand{position:absolute;left:22px;top:24px;font-size:20px;font-weight:700;color:var(--navy)}
  .footer-slash{position:absolute;left:245px;top:0;width:30px;height:73px;background:var(--orange);transform:skewX(-18deg)}
  .footer-bar{position:absolute;left:596px;top:0;width:24px;height:73px;background:var(--orange)}
  .visit{position:absolute;left:622px;top:14px;width:214px;text-align:center}
  .visit .label{font-size:16px;color:var(--navy);font-weight:500}
  .visit .url{font-size:13.5px;color:var(--orange);font-weight:500;margin-top:3px;white-space:nowrap}
</style>
</head>
<body>
<main class="flyer">
  <header class="masthead">
    <span class="brand-name">Cobalt Ridge Buildworks</span>
    <span class="brand-dot"></span>
  </header>

  <section class="about">
    <div class="about-stripe-navy"></div>
    <div class="about-stripe-orange"></div>
    <h1 class="about-title"><span class="accent">ABOUT</span> US</h1>
    <div class="about-rule"></div>
    <p class="about-copy">Cobalt Ridge Buildworks (CRB) is a leading National Project Management consulting firm. With a commitment to service and effective management, we at CRB offer a full range of professional services. Our team of consultants can support your diverse projects from Pre-Project Planning to Commissioning.<br>CRB offers assistance in the detailed processes of project management: creating work breakdown structures and baseline control budgets, cost forecasts, cash flow analysis, quality control, planning, scheduling, estimating and change control management. We partner with you to achieve the desired output.</p>
  </section>

  <section class="profile">
    <div class="block">
      <h2>Mission</h2>
      <p>CRB will provide exceptional project management services to our clients and add value by being an integral partner, whose focus is on transparency and quality.</p>
    </div>
    <div class="block">
      <h2 class="navy">Vision</h2>
      <p>To be a leader in project management and a preferred vendor for our clients.</p>
    </div>
    <div class="block">
      <h2>Core Value</h2>
      <ul>
        <li>Loyalty and Commitment</li>
        <li>Safety and Quality</li>
        <li>Respect</li>
        <li>Teamwork</li>
      </ul>
    </div>
    <div class="block" style="margin-top:30px">
      <h2 class="navy">Services</h2>
      <p>CRB offers a wide range of services to improve project performance and cost effectiveness, to ensure our clients success. Our services extend from the early stages of pre-project planning and development, to successful execution.</p>
    </div>
  </section>

  <section class="offer">
    <h3>We offer specialized services<br>in the following areas:</h3>
    <div class="offer-rule"></div>
    <svg width="400" height="545" viewBox="0 0 400 545">
      <g fill="none" stroke="var(--orange)" stroke-width="2">
        <polyline points="24,122 83,162 32,222 96,272 36,327 107,380 42,437 116,497"/>
      </g>
      <g fill="#fff" stroke="var(--orange)" stroke-width="2.5">
        <circle cx="24" cy="122" r="18"/><circle cx="83" cy="162" r="18"/>
        <circle cx="32" cy="222" r="18"/><circle cx="96" cy="272" r="18"/>
        <circle cx="36" cy="327" r="18"/><circle cx="107" cy="380" r="18"/>
        <circle cx="42" cy="437" r="18"/><circle cx="116" cy="497" r="18"/>
      </g>
      <g fill="var(--navy)">
        <circle cx="24" cy="122" r="8"/><circle cx="83" cy="162" r="8"/>
        <circle cx="32" cy="222" r="8"/><circle cx="96" cy="272" r="8"/>
        <circle cx="36" cy="327" r="8"/><circle cx="107" cy="380" r="8"/>
        <circle cx="42" cy="437" r="8"/><circle cx="116" cy="497" r="8"/>
      </g>
    </svg>
    <span class="service" style="left:48px;top:113px">Technical Engineering Support</span>
    <span class="service" style="left:107px;top:153px">Cost Planning and Management</span>
    <span class="service" style="left:56px;top:213px">Financial Reporting</span>
    <span class="service" style="left:120px;top:263px">Project Set Up</span>
    <span class="service" style="left:60px;top:318px">Owners Oversight</span>
    <span class="service" style="left:131px;top:371px">Construction and Contract Management</span>
    <span class="service" style="left:66px;top:428px">Operational Excellence and Improvement</span>
    <span class="service wrap" style="left:140px;top:481px">Insertion of key members of CRB Staff (Strategic Placement) within your client team</span>
  </section>

  <footer class="footer">
    <span class="footer-brand">Cobalt Ridge Buildworks</span>
    <div class="footer-slash"></div>
    <div class="footer-bar"></div>
    <div class="visit">
      <div class="label">Visit Us</div>
      <div class="url">www.cobaltridgebuildworks.com</div>
    </div>
  </footer>
</main>
</body>
</html>
```